Client Fulfillment Flyer

This is a document used for internal purposes ie it is not distributed to clients. We would like it to have some colour, images etc. We are in the financial services industry, Ballarat, Victoria, Australia. www.torvelle.com.au and www.torvelleagri.com.au

Target Market(s)

Internal training document

Industry/Entity Type

Finance And Accounting

Colors
3176b5

```html
<!DOCTYPE html>
<html lang="en">
<head>
<meta charset="utf-8">
<title>Torvelle &amp; Co Client Fulfillment System</title>
<link href="https://fonts.googleapis.com/css2?family=Raleway:wght@300;400;500;600;700&display=swap" rel="stylesheet">
<style>
:root{
  --brand:#3176b5;
  --brand-dark:#1f5a96;
  --ink:#2a2f36;
  --muted:#5a6270;
  --row:#eef1f5;
  --paper:#ffffff;
  --stage:#dcdde0;
  --wheat:#b89a62;
  --field:#7f9a52;
  --crowd:#4b6e9c;
  --yard:#8c7d66;
  --sky:#8fb4d8;
  --herd:#3a3d42;
}
*{box-sizing:border-box;margin:0;padding:0}
html,body{width:1200px;height:1200px;overflow:hidden;background:var(--stage);font-family:"Raleway",sans-serif;color:var(--ink)}
.sheet-grid{position:absolute;left:0;top:0;width:1200px;height:1200px;display:grid;grid-template-columns:repeat(4,282px);grid-template-rows:repeat(2,400px);column-gap:14px;row-gap:40px;padding:170px 15px;overflow:hidden}
.page{position:relative;width:282px;height:400px;background:var(--paper);box-shadow:0 6px 14px rgba(0,0,0,.25);overflow:hidden;padding:18px 20px 0}
.page-footer{position:absolute;left:0;right:0;bottom:0;height:40px;background:var(--brand);display:flex;align-items:center;justify-content:space-between;padding:0 14px;color:#fff;font-size:3.5px}
.wordmark{display:flex;align-items:center;gap:3px;font-weight:600;color:#fff;font-size:7px;letter-spacing:.3px}
.wordmark .dot{width:9px;height:9px;border-radius:50%;background:#fff}
.wordmark.blue{color:var(--brand)}
.wordmark.blue .dot{background:var(--brand)}
.title{font-size:6px;font-weight:600;color:var(--ink);border-bottom:1px solid var(--brand);padding-bottom:2px;margin-bottom:6px;text-transform:uppercase}
.label{font-size:4.2px;color:var(--muted);text-transform:uppercase;border-bottom:.6px solid #ccd;padding-bottom:1.5px;margin:5px 0 3px}
.heading{font-size:6px;font-weight:600;color:var(--brand-dark);border-bottom:1px solid var(--brand);padding-bottom:2px;margin:6px 0 4px}
p,li{font-size:3.4px;line-height:1.45;color:var(--muted);margin-bottom:2.5px}
ul,ol{padding-left:9px;margin-bottom:3px}
.photo{width:100%;margin:4px 0}
.photo.wheat{background:linear-gradient(180deg,#c9c2ae 0%,#a88f5c 45%,#6f5a34 100%)}
.photo.field{background:linear-gradient(180deg,#9db15f 0%,var(--field) 60%,#56702f 100%)}
.photo.crowd{background:linear-gradient(160deg,#2d4f83 0%,var(--crowd) 55%,#c9cf3f 100%)}
.photo.yard{background:linear-gradient(180deg,#b6a58a 0%,var(--yard) 60%,#5e5241 100%)}
.photo.farmer{background:linear-gradient(180deg,var(--sky) 0%,#d9e3ee 40%,#b09a6c 70%,#7a6a4b 100%)}
.photo.herd{background:linear-gradient(180deg,var(--herd) 0%,#5a5c5e 55%,#a89c86 100%)}
.cover{padding:0}
.cover-band{height:104px;background:var(--brand);display:flex;align-items:center;justify-content:center}
.cover-band .wordmark{font-size:10px}
.cover-band .wordmark .dot{width:14px;height:14px}
.cover-title{height:84px;display:flex;flex-direction:column;justify-content:center;align-items:center;font-weight:300;font-size:9px;color:var(--brand-dark);letter-spacing:.3px;line-height:1.35}
.cover .photo{height:172px;margin:0}
.tbl{font-size:3.4px;margin-top:3px}
.tr{display:grid;grid-template-columns:1fr 14px 20px 20px 20px;align-items:center;min-height:7px;padding:1px 2px;border-bottom:.4px solid #d7dbe2;color:var(--ink)}
.tr:nth-child(odd){background:var(--row)}
.tr.head{background:var(--brand);color:#fff;min-height:16px;align-items:start;font-size:3.2px}
.tr i{font-style:normal;text-align:center;color:var(--ink)}
.tr.head i{color:#fff}
.quote{position:relative;padding:0 12px}
.quote::before,.quote::after{position:absolute;font-size:22px;font-weight:700;color:var(--brand-dark);line-height:1}
.quote::before{content:"\201C";left:-2px;top:-2px}
.quote::after{content:"\201D";right:-2px;bottom:-14px}
.quote p{font-style:italic}
.center-mark{display:flex;justify-content:center;margin:4px 0 12px}
.center-mark .wordmark{font-size:8px}
</style>
</head>
<body>
<main class="sheet-grid">

  <section class="page cover">
    <div class="cover-band"><span class="wordmark"><span class="dot"></span>TORVELLE &amp; CO</span></div>
    <div class="cover-title"><span>THE TORVELLE &amp; CO</span><span>CLIENT FULFILLMENT SYSTEM</span></div>
    <div class="photo wheat" role="img" aria-label="Close-up photograph of a ripe wheat field at golden hour"></div>
    <footer class="page-footer"><span>www.torvelle.com.au</span><span>www.torvelleagri.com.au</span></footer>
  </section>

  <section class="page">
    <div class="title">The Torvelle &amp; Co Client Fulfillment System</div>
    <div class="label">Client Fulfillment</div>
    <p>We are primarily a service based business however the product we sell is Client Fulfillment.</p>
    <p>Client Fulfillment in simple terms means providing the services to satisfy client requirements and expectations. Our aim is to not only satisfy but exceed them.</p>
    <p>The Client Fulfillment system is the methodology through which we deliver the result we have promised to deliver.</p>
    <p>Why is this important? In order to achieve our Core Purpose and Vision, delivering Client Fulfillment is essential.</p>
    <div class="photo field" style="height:104px" role="img" aria-label="Photograph of a tractor baling hay in a green paddock"></div>
    <div class="label">The Client Fulfillment Process</div>
    <p>The areas we focus on to deliver Client Fulfillment are:</p>
    <ul>
      <li>Understanding Core Purpose, Core Values, Vision and Why</li>
      <li>Client Management and Communication</li>
      <li>The Basics</li>
      <li>The Are You Financially Secure Process</li>
      <li>The Right People Doing the Right Work</li>
    </ul>
    <div class="heading">Understanding Core Purpose, Core Values, Vision and Why</div>
    <div class="label">Client Fulfillment</div>
    <p>These terms can be overwhelming and confusing but to deliver Client Fulfillment it is important to understand what it all means and how it all connects.</p>
    <p>Our Core Purpose and Core Values are the foundation of our business. We have a clear Vision of where we want the business to go, that is what it will look like in ten years. Underlying this is our Why.</p>
    <footer class="page-footer"><span>Page 2 of 10</span><span class="wordmark"><span class="dot"></span>TORVELLE &amp; CO</span></footer>
  </section>

  <section class="page">
    <div class="center-mark"><span class="wordmark blue"><span class="dot"></span>TORVELLE &amp; CO</span></div>
    <div class="heading" style="font-weight:500">Our Vision. &nbsp;What is it?</div>
    <div class="label">This is our vision across the entire Torvelle &amp; Co business:</div>
    <div class="quote">
      <p>To provide all businesses and individuals with the opportunity to achieve financial security.</p>
      <p>Our business is designed so people can access all the services required to achieve financial security.</p>
      <p>We are a motivated team that embraces change and technology along with having the knowledge, skills and expertise to help committed clients.</p>
      <p>We do not limit the number of people we can help and distance is not a barrier.</p>
      <p>Our goal is to be helping at least 5,000 client family groups along their journey to reach their financial goals.</p>
    </div>
    <div class="photo crowd" style="height:104px;margin-top:10px" role="img" aria-label="Photograph of students in hi-vis vests at a farm expo stand"></div>
    <div class="label">How are we going to achieve our vision?</div>
    <p>We need to work in an effective and efficient manner to achieve this vision.</p>
    <p>We break the vision down into smaller plans and action items. We then prioritise these steps with responsibility and accountability.</p>
    <p>As each step is in progress and being completed we are getting closer to achieving our vision.</p>
    <p>Our core purpose states the reason we exist. The core values are our fundamental beliefs.</p>
    <footer class="page-footer"><span>Page 3 of 10</span><span class="wordmark"><span class="dot"></span>TORVELLE &amp; CO</span></footer>
  </section>

  <section class="page">
    <p>Understanding our Why helps to provide a connection with our vision and purpose. Rather than focusing on what we do and how we do it, we need to understand why we do it.</p>
    <p>If you understand Why, it gives a greater purpose to the work you do every day. It is a mindset: are you at work to process transactions or are you helping committed clients achieve financial security?</p>
    <p>We have Service Standards and Culture Standards. These are the basic rules and expectations of all team members.</p>
    <div class="photo yard" style="height:80px" role="img" aria-label="Photograph of a working dog and sheep in shearing shed yards"></div>
    <div class="heading">Client Management and Communication</div>
    <p>Client Management and Communication in the context of Client Fulfillment is understanding our client needs, requirements and expectations and ensuring delivery is consistent with our Core Purpose.</p>
    <p>People like to feel valued and not just a small part of a big business. Our CRM and technology mean we can reach out to individuals with relevant information.</p>
    <div class="label">The 10 Non Negotiables:</div>
    <ol>
      <li>Client phone calls and emails are replied to the same day received.</li>
      <li>Work is allocated / delegated to the appropriate team member.</li>
      <li>Systems, processes and checklists are used.</li>
      <li>All compliance work and lodgements are completed on time and by due dates.</li>
      <li>A fee proposal is communicated to client before starting work.</li>
      <li>The AYFS requirements are completed and updated annually.</li>
      <li>Annual Accounts meeting occurs once annual financial statements are completed.</li>
      <li>There is a minimum of monthly communication to clients under management.</li>
      <li>Prior to going on leave client work is planned and arrangements are put in place to ensure clients are looked after.</li>
      <li>We are outcome focused rather than timesheet focused.</li>
    </ol>
    <footer class="page-footer"><span>Page 4 of 10</span><span class="wordmark"><span class="dot"></span>TORVELLE &amp; CO</span></footer>
  </section>

  <section class="page">
    <div class="heading">The Right People Doing the Right Work</div>
    <ol>
      <li>A team is a group of individuals all working together for a common purpose. Each team member has a role in the team.</li>
      <li>To deliver Client Fulfillment it is important that we work as a team and understand our role.</li>
      <li>This will ensure as a team we are directing our time and focus in the way required.</li>
      <li>Much of our time is invested completing The Basics. However on a daily basis there is much more to do to help clients.</li>
      <li>Below is a table of the many jobs and tasks we do on a daily basis and the team member role.</li>
    </ol>
    <div class="heading" style="font-size:4.6px;color:var(--ink)">1. &nbsp;&nbsp;KEY INFORMATION</div>
    <div class="tbl">
      <div class="tr head"><span></span><i>CSM</i><i>Manila Accountant</i><i>Accountant</i><i>Senior Manager / Partner</i></div>
      <div class="tr"><span>Contacting clients for missing information</span><i>✓</i><i></i><i></i><i></i></div>
      <div class="tr"><span>Changes to database / CRM</span><i>✓</i><i></i><i></i><i></i></div>
      <div class="tr"><span>Returning client records</span><i>✓</i><i></i><i></i><i></i></div>
      <div class="tr"><span>Preparing Balance Date Checklists</span><i>✓</i><i></i><i></i><i></i></div>
      <div class="tr"><span>Fee proposal draft preparation and send to client once final</span><i>✓</i><i></i><i></i><i></i></div>
      <div class="tr"><span>Job set up</span><i>✓</i><i></i><i></i><i></i></div>
      <div class="tr"><span>Confirm fee proposal details, explain benefit to client and value</span><i></i><i></i><i>✓</i><i>✓</i></div>
      <div class="tr"><span>Setting Due Dates for all jobs in workflow program</span><i>✓</i><i></i><i></i><i></i></div>
      <div class="tr"><span>Collating information to send to banks, finance co's etc</span><i>✓</i><i></i><i></i><i></i></div>
      <div class="tr"><span>Setting and managing Start Dates and To-do Dates in workflow program</span><i></i><i></i><i>✓</i><i></i></div>
      <div class="tr"><span>Manage workflow to meet client expectations and team sales budget</span><i></i><i></i><i>✓</i><i>✓</i></div>
      <div class="tr"><span>Communicate workflow concerns and bottlenecks before they become an issue</span><i></i><i></i><i>✓</i><i></i></div>
      <div class="tr"><span>Dealing with Tax Office correspondence</span><i>✓</i><i></i><i></i><i></i></div>
      <div class="tr"><span>Contacting the Tax Office</span><i>✓</i><i></i><i></i><i></i></div>
    </div>
    <footer class="page-footer"><span>Page 5 of 10</span><span class="wordmark"><span class="dot"></span>TORVELLE &amp; CO</span></footer>
  </section>

  <section class="page">
    <div class="tbl" style="margin-top:20px">
      <div class="tr head"><span></span><i>CSM</i><i>Manila Accountant</i><i>Accountant</i><i>Senior Manager / Partner</i></div>
      <div class="tr"><span>Advising clients of PAYG instalment amounts and due dates</span><i>✓</i><i></i><i></i><i></i></div>
      <div class="tr"><span>Printing, binding financial statements, tax returns and reports etc</span><i>✓</i><i></i><i></i><i></i></div>
      <div class="tr"><span>Advising clients of TFN, ABN, GST registrations etc</span><i>✓</i><i></i><i></i><i></i></div>
      <div class="tr"><span>Advising clients of tax assessment notices</span><i>✓</i><i></i><i></i><i></i></div>
      <div class="tr"><span>Invoicing and job completion</span><i>✓</i><i></i><i></i><i></i></div>
      <div class="tr"><span>Monitoring Activity Statement lodgments</span><i>✓</i><i></i><i></i><i></i></div>
      <div class="tr"><span>Manage new entity set ups</span><i>✓</i><i></i><i></i><i></i></div>
      <div class="tr"><span>Monitor Tax Office lodgment and payment dates</span><i>✓</i><i></i><i></i><i></i></div>
      <div class="tr"><span>Attend to Registry requirements</span><i>✓</i><i></i><i></i><i></i></div>
      <div class="tr"><span>Managing HN portal upload and download</span><i>✓</i><i></i><i></i><i></i></div>
      <div class="tr"><span>Prepare checklists</span><i>✓</i><i></i><i></i><i></i></div>
      <div class="tr"><span>Save information to HN</span><i>✓</i><i>✓</i><i></i><i></i></div>
      <div class="tr"><span>Organising client meetings</span><i>✓</i><i></i><i></i><i></i></div>
      <div class="tr"><span>Bookkeeping function – process Ledgerly monthly / quarterly</span><i></i><i>✓</i><i></i><i></i></div>
      <div class="tr"><span>Process monthly / quarterly journal entries – depreciation, equipment finance etc</span><i></i><i>✓</i><i></i><i></i></div>
      <div class="tr"><span>Prepare financial statements</span><i></i><i>✓</i><i>✓</i><i></i></div>
      <div class="tr"><span>Prepare tax returns</span><i></i><i>✓</i><i>✓</i><i></i></div>
      <div class="tr"><span>Prepare activity statements</span><i></i><i>✓</i><i>✓</i><i></i></div>
      <div class="tr"><span>Review work completed by Manila Accountant</span><i></i><i></i><i>✓</i><i></i></div>
      <div class="tr"><span>Complete final review of Annual Accounts</span><i></i><i></i><i></i><i>✓</i></div>
      <div class="tr"><span>Prepare tax planning</span><i></i><i>✓</i><i>✓</i><i></i></div>
      <div class="tr"><span>Review tax planning</span><i></i><i></i><i></i><i>✓</i></div>
      <div class="tr"><span>Conduct tax planning meeting</span><i></i><i></i><i></i><i>✓</i></div>
      <div class="tr"><span>Welfare Office applications – draft</span><i>✓</i><i></i><i></i><i></i></div>
      <div class="tr"><span>Welfare Office application – completion</span><i></i><i></i><i>✓</i><i></i></div>
      <div class="tr"><span>Manage new client on boarding</span><i>✓</i><i></i><i></i><i></i></div>
      <div class="tr"><span>Ledgerly set up, bank feeds etc</span><i>✓</i><i></i><i></i><i></i></div>
      <div class="tr"><span>Ledgerly training, chart of accounts set up etc</span><i></i><i>✓</i><i>✓</i><i></i></div>
      <div class="tr"><span>Save AYFS schedule and set up for current year</span><i>✓</i><i></i><i></i><i></i></div>
    </div>
    <footer class="page-footer"><span>Page 6 of 10</span><span class="wordmark"><span class="dot"></span>TORVELLE &amp; CO</span></footer>
  </section>

  <section class="page">
    <div class="tbl">
      <div class="tr head"><span></span><i>CSM</i><i>Manila Accountant</i><i>Accountant</i><i>Senior Manager / Partner</i></div>
      <div class="tr"><span>Check other divisions have updated relevant AYFS schedules</span><i>✓</i><i></i><i></i><i></i></div>
      <div class="tr"><span>Update AYFS schedules</span><i></i><i></i><i>✓</i><i></i></div>
      <div class="tr"><span>Review AYFS schedules</span><i></i><i></i><i></i><i>✓</i></div>
      <div class="tr"><span>Conduct Annual Account meeting</span><i></i><i></i><i></i><i>✓</i></div>
      <div class="tr"><span>Prepare team management reports</span><i>✓</i><i></i><i>✓</i><i></i></div>
      <div class="tr"><span>Prepare monthly client communication material</span><i></i><i></i><i></i><i>✓</i></div>
    </div>
    <div class="photo farmer" style="height:166px;margin-top:14px" role="img" aria-label="Photograph of a farmer and his dog at a paddock gate under a cloudy sky"></div>
    <footer class="page-footer"><span>Page 7 of 10</span><span class="wordmark"><span class="dot"></span>TORVELLE &amp; CO</span></footer>
  </section>

  <section class="page">
    <div class="photo herd" style="height:106px;margin-top:14px" role="img" aria-label="Photograph of black and white dairy cows feeding at a trough"></div>
    <div class="heading" style="margin-top:8px">The Basics</div>
    <p>Don't let the heading give the impression these tasks have low importance. The term Basics represents work clients expect to be completed with minimal fuss.</p>
    <p>The Basics include:</p>
    <ul>
      <li>Activity statement preparation and lodgement</li>
      <li>Taxation return lodgement</li>
      <li>Financial statement preparation</li>
      <li>Tax planning</li>
      <li>Tax Office compliance</li>
      <li>SRO compliance</li>
      <li>Welfare Office compliance</li>
    </ul>
    <p>This work is the main reason accountants have clients. Clients have to lodge information with the Tax Office and SRO. Completing this work accurately and efficiently is important.</p>
    <p>This work is not necessarily difficult. It is more about being organised, collating and checking information throughout the year.</p>
    <p>Systems, processes and checklists are critical for the controlled flow of this work. The volume of work is high with lodgement deadlines to be met.</p>
    <p>Having access to this level of financial information is a privileged position. This information can be used to help clients further.</p>
    <div class="heading" style="margin-top:10px">Quality Control</div>
    <footer class="page-footer"><span>Page 8 of 10</span><span class="wordmark"><span class="dot"></span>TORVELLE &amp; CO</span></footer>
  </section>

</main>
</body>
</html>
```